Lumara Health & Wellness Business Card Design

We would like to create business cards matching with our new logo design. The card should be professional looking but still have a playful side and something that would be eye catching. We are planing to open a luxury medical spa and looking to create a design based on this new logo. We are looking for a design that shows off luxury but not be gold in color. Also, while we are a more female oriented medical center we do have men that come in for our services and it should be be too feminine.

Target Market(s)

Health & Wellness. Medical patients. Luxury spa

Industry/Entity Type

Health And Wellness

Contact Information for Business Card

It should have the logo design in the front of card and back of card should have our contact information. Our current colors are peach/ coral, teal, and gray. We are looking for a modern looking design.

Font styles to use
Script

Colors
32a6d6
e667a6
86cfc6
fece3e

Requirements
Must have
• It should have our logo design. We would prefer to have a more modern look to the card.
Nice to have
• Eye-Catching Design on the personable side but still classy.
Should not have
• At this point we are looking for the best design. It should not have color purple.

```html
<!DOCTYPE html>
<html lang="en">
<head>
<meta charset="UTF-8">
<title>Lumara Health &amp; Wellness – Business Card</title>
<link rel="stylesheet" href="https://fonts.googleapis.com/css2?family=Montserrat:wght@400&display=swap">
<style>
  :root {
    --backdrop: #1f1f21;
    --card-teal: #73b5a3;
    --foil-silver: #eef1f0;
    --foil-soft: rgba(238, 241, 240, 0.9);
  }
  * { margin: 0; padding: 0; box-sizing: border-box; }
  html, body {
    width: 1200px;
    height: 900px;
    overflow: hidden;
    background: var(--backdrop);
  }
  .canvas {
    position: relative;
    width: 1200px;
    height: 900px;
    font-family: 'Montserrat', sans-serif;
    color: var(--foil-silver);
  }
  .card {
    position: absolute;
    left: 300px;
    width: 600px;
    height: 340px;
    background: var(--card-teal);
    border-radius: 30px;
  }
  .card--front { top: 90px; }
  .card--back { top: 470px; }

  .brand-name {
    font-family: 'Montserrat', sans-serif;
    font-weight: 400;
    color: var(--foil-silver);
    letter-spacing: 0.06em;
    line-height: 1.25;
    text-align: center;
  }
  .card--front .brand-name {
    position: absolute;
    left: 0; right: 0;
    top: 50%;
    transform: translateY(-50%);
    font-size: 32px;
  }
  .brand-name .brand-line { display: block; }
  .brand-name .brand-line--sub { font-size: 0.55em; letter-spacing: 0.14em; }

  .card--back .brand-name {
    position: absolute;
    left: 30px;
    width: 250px;
    top: 50%;
    transform: translateY(-50%);
    font-size: 26px;
  }
  .divider {
    position: absolute;
    left: 300px;
    top: 80px;
    width: 2px;
    height: 180px;
    background: var(--foil-soft);
  }
  .contact {
    position: absolute;
    left: 326px;
    top: 100px;
  }
  .contact__name {
    font-size: 26px;
    letter-spacing: 0.02em;
    line-height: 1.05;
  }
  .contact__title {
    font-size: 15px;
    letter-spacing: 0.05em;
    margin-bottom: 22px;
  }
  .contact__row {
    display: flex;
    align-items: center;
    gap: 12px;
    font-size: 15px;
    margin-bottom: 12px;
  }
  .contact__icon { width: 16px; height: 14px; flex: none; }
</style>
</head>
<body>
<main class="canvas">
  <section class="card card--front" aria-label="Card front">
    <h1 class="brand-name">
      <span class="brand-line">Lumara</span>
      <span class="brand-line brand-line--sub">HEALTH &amp; WELLNESS</span>
    </h1>
  </section>

  <section class="card card--back" aria-label="Card back">
    <p class="brand-name">
      <span class="brand-line">Lumara</span>
      <span class="brand-line brand-line--sub">HEALTH &amp; WELLNESS</span>
    </p>
    <div class="divider"></div>
    <div class="contact">
      <p class="contact__name">YOUR NAME</p>
      <p class="contact__title">JOB TITLE</p>
      <p class="contact__row">
        <svg class="contact__icon" viewBox="0 0 16 14" aria-hidden="true">
          <path d="M1 4 Q8 -1 15 4 L13 6 L11 4.5 L5 4.5 L3 6 Z" fill="#eef1f0"/>
          <rect x="3" y="7" width="10" height="6" rx="1" fill="#eef1f0"/>
        </svg>
        <span>000 000 0000</span>
      </p>
      <p class="contact__row">
        <svg class="contact__icon" viewBox="0 0 16 14" aria-hidden="true">
          <rect x="1" y="2" width="14" height="10" rx="1" fill="#eef1f0"/>
          <path d="M1.5 2.5 L8 8 L14.5 2.5" fill="none" stroke="#73b5a3" stroke-width="1.3"/>
        </svg>
        <span>youremail@xyz.com</span>
      </p>
    </div>
  </section>
</main>
</body>
</html>
```